Maple Roadway Handbook
2nd Edition
Love #26 and #28 and #33
The graphics are original, they don't make it appear as if I am promoting Driving drunk and they have good graphic appeal.
I don't want to seem like I am promoting Driving drunk so #32 (and #19 and #29)seem to dance a little too close to the edge.
#25 -Awesome job! I need you to post a version with
1) No text on the back cover
2) No publisher's logo and location
3) No ISBN number or bar code
3) No photo (leave the white box under neath the photo)
4) No text on the spine
I like that this cover is implementing a graphic of some sort (the swirly thingy). I am not wild about brown though.
I would recommend getting rid of the glow around the subtext and the underline on the very top. However, I don't know that I would choose this design idea even if it was executed perfectly.
Take your designs in a whole new direction. The fonts and text locations are easy to tweak, the hard part is thinking of a unique graphic to make the focus of the cover. Most of the submissions so far have implement text and colored rectangles, so try to think of a stock photo or a graphic or a shape that will grab the attention, and then worry about the text later.
I am hoping for someone to submit designs that implement graphics, photos, or something more than a few two-toned rectangles.
#6 and #7 are nearly exact copies of the first edition only the color is changed slightly. I will not choose a submission that is essentially a version of the first edition.
#5 This is almost an exact replica of the first edition only its blue. I am not interested in designs that look similar to the first edition.
#3 The big gold start is not a wholly bad element, but I think having it front and center, makes it too prominent.
General Comment.
The Back cover of this book will have:
1) an ISBN
2)Text
3) A photo
4)the publishers logo
HOWEVER - The design we choose will not have any of those elements included. We will be altering the photo, text, ect. and pasting then on top of the design chosen here.
I think it is really helpful to include some place holder, text, photos, isbn ect. on your initial submissions so we can see how the elements will fit into your back cover layout, but once we have zeroed in on a design we like, we will need to have those elements removed.
#2 and #3 I am not wild about the colors.
#1 The title font is a bit cartoonist, which doesn't work well for a law firm trying to impress clientele. Also, all the text is crammed into the top of the cover, leaving a large blank space in the bottom 2/3.
I would reexamine your font selection. take a look at some professional text books and reference books. I would also consider how to balance the test at the top with the emptiness at the bottom. Once again, take a look at other professional text and reference books for ideas.
#4 I like the the colors and the different color blocks, but I am not wild about the word "Handbook" written vertically. I feel like something should be written there, but I am not sure about what, and the word "handbook" is not something that is particularly important or deserves emphasis.
Submissions #4,3,& 2 I appreciate you doing a mock up of the back page, but the your final submission should not have the text, picture, publisher's logo, or the ISBN. All of those items will be pasted ontop of your submission after the fact. You can go ahead an add them just so I can see what it would look like, but final submission would need to be altered.

```html
<!DOCTYPE html>
<html lang="en">
<head>
<meta charset="utf-8">
<title>The Maple Roadway Handbook – Cover</title>
<link rel="stylesheet" href="https://fonts.googleapis.com/css2?family=Open+Sans:wght@400;600;700;800&family=PT+Sans:wght@400;700&display=swap">
<style>
  :root {
    --stage: #000000;
    --spine: #5e5850;
    --band-grey: #a3a5a8;
    --sky-top: #a9cdea;
    --sky-mid: #dcecf8;
    --paper: #ffffff;
    --ink: #111111;
    --title-ink: #3a3a3a;
    --edition-band: rgba(40, 40, 40, 0.72);
    --subtitle-band: rgba(70, 70, 70, 0.55);
    --scene-top: #b8c3ca;
    --scene-mid: #8f9c98;
    --scene-low: #b3bcc2;
    --scene-base: #dde7ef;
  }
  html, body {
    margin: 0;
    padding: 0;
    width: 1200px;
    height: 883px;
    overflow: hidden;
    background: var(--stage);
  }
  .canvas {
    position: relative;
    width: 1200px;
    height: 883px;
    background: var(--stage);
  }

  /* Back cover */
  .back-cover {
    position: absolute;
    left: 72px;
    top: 65px;
    width: 487px;
    height: 744px;
    background: linear-gradient(180deg, var(--sky-top) 0%, var(--sky-mid) 25%, var(--paper) 55%, var(--sky-mid) 85%, var(--sky-top) 100%);
    font-family: "PT Sans", Tahoma, sans-serif;
    color: var(--ink);
    overflow: hidden;
  }
  .spine {
    position: absolute;
    left: 0;
    top: 0;
    width: 34px;
    height: 100%;
    background: var(--spine);
  }
  .back-band {
    position: absolute;
    left: 34px;
    right: 0;
    background: var(--band-grey);
  }
  .back-band--top { top: 19px; height: 43px; }
  .back-band--bottom { top: 667px; height: 53px; }
  .label {
    position: absolute;
    font-size: 19px;
    line-height: 1;
  }
  .label--text1 { left: 50px; top: 31px; font-weight: 700; }
  .label--text2 { left: 293px; top: 85px; }
  .label--text3 { left: 50px; top: 346px; }
  .label--logo  { left: 65px; top: 600px; }
  .label--isbn  { left: 360px; top: 600px; }
  .photo-slot {
    position: absolute;
    left: 19px;
    top: 86px;
    width: 161px;
    height: 155px;
    border: 3px solid var(--ink);
    background: var(--paper);
    box-sizing: border-box;
  }
  .photo-slot .label { left: 43px; top: 14px; font-weight: 700; }

  /* Front cover */
  .front-cover {
    position: absolute;
    left: 648px;
    top: 65px;
    width: 487px;
    height: 744px;
    overflow: hidden;
    background: linear-gradient(180deg, #7fb3e0 0%, #b9d7ef 18%, #e3eef7 34%);
    font-family: "Open Sans", Verdana, sans-serif;
  }
  .cover-scene {
    position: absolute;
    left: 0;
    top: 200px;
    width: 100%;
    height: 544px;
    background: linear-gradient(180deg, var(--scene-top) 0%, var(--scene-mid) 45%, var(--scene-low) 78%, var(--scene-base) 100%);
  }
  .cover-title {
    position: absolute;
    left: 0;
    top: 60px;
    width: 100%;
    margin: 0;
    text-align: center;
    font-weight: 800;
    font-size: 44px;
    line-height: 1.25;
    color: var(--title-ink);
    letter-spacing: 0.5px;
  }
  .edition-band {
    position: absolute;
    left: 0;
    top: 272px;
    width: 100%;
    height: 50px;
    background: var(--edition-band);
    color: var(--paper);
    font-weight: 700;
    font-size: 21px;
    line-height: 50px;
    text-align: center;
  }
  .subtitle-band {
    position: absolute;
    left: 0;
    top: 350px;
    width: 100%;
    height: 118px;
    background: var(--subtitle-band);
    display: flex;
    align-items: center;
    justify-content: center;
  }
  .subtitle {
    margin: 0;
    width: 410px;
    color: var(--paper);
    font-weight: 400;
    font-size: 19px;
    line-height: 31px;
    text-align: center;
  }
  .author {
    position: absolute;
    left: 0;
    top: 680px;
    width: 100%;
    text-align: center;
    font-weight: 700;
    font-size: 20px;
    line-height: 26px;
    color: #2b2b2b;
  }
</style>
</head>
<body>
<main class="canvas">
  <section class="back-cover" aria-label="Back cover layout">
    <div class="spine"></div>
    <div class="back-band back-band--top"></div>
    <span class="label label--text1">Text 1</span>
    <div class="photo-slot"><span class="label">Photo</span></div>
    <span class="label label--text2">Text 2</span>
    <span class="label label--text3">Text 3</span>
    <span class="label label--logo">Logo</span>
    <span class="label label--isbn">ISBN</span>
    <div class="back-band back-band--bottom"></div>
  </section>

  <section class="front-cover" aria-label="Front cover">
    <div class="cover-scene" role="img" aria-label="Photo area: a driver seated behind the wheel of a car, trees in the background"></div>
    <h1 class="cover-title">The Maple Roadway<br>Handbook</h1>
    <div class="edition-band">Second Edition</div>
    <div class="subtitle-band">
      <p class="subtitle">Answers to 14 Common Questions and Everything Else You Need to Know About DUIs</p>
    </div>
    <div class="author">Thomas R. Barwick, Esq.</div>
  </section>
</main>
</body>
</html>
```